Album art for soul / electronic band

Album art for a singer / producer duo. Art should be similar to the copper lantern album art and be consistent with the color scheme in the attached band photo. The name of the album is cantarela (portuguese for delicate). Please do not include the photo in your design. Design should center around water.

Target Market(s)

Gen X / Millenial soul music fans

Industry/Entity Type

music

Font styles to use
Sans Serif

Requirements
Must have
• Clean modern look, photo or artwork.
Nice to have
• It should look like album art from groups in the same genre such as the Copper Lantern, Harbortide, K. Denby, Odo Varne
Should not have
• band photo, musical notes, any music iconography

```html
<!DOCTYPE html>
<html lang="en">
<head>
<meta charset="utf-8">
<title>Ilka Sorren — Cantarela</title>
<link rel="stylesheet" href="https://fonts.googleapis.com/css2?family=Montserrat:wght@200;300;600&display=swap">
<style>
  :root {
    --sky-top: #3f5f68;
    --sky-mist: #7f97a0;
    --sky-haze: #9aa9b8;
    --sun-core: #f4f6f0;
    --sun-glow: #d8e27a;
    --forest-deep: #10160f;
    --forest-moss: #2c3a22;
    --river-teal: #3f7b88;
    --river-light: #6fb7bf;
    --ink-white: #ffffff;
  }
  html, body {
    margin: 0;
    padding: 0;
    width: 1200px;
    height: 1200px;
    overflow: hidden;
    background: var(--forest-deep);
  }
  .album-cover {
    position: relative;
    width: 1200px;
    height: 1200px;
    overflow: hidden;
  }
  .cover-artwork {
    position: absolute;
    inset: 0;
    background:
      radial-gradient(ellipse 170px 140px at 420px 340px, var(--sun-core) 0%, rgba(244,246,240,0.6) 40%, rgba(216,226,122,0) 100%),
      radial-gradient(ellipse 330px 220px at 400px 390px, rgba(216,226,122,0.65) 0%, rgba(216,226,122,0) 100%),
      radial-gradient(ellipse 520px 260px at 720px 700px, rgba(111,183,191,0.75) 0%, rgba(63,123,136,0.55) 50%, rgba(63,123,136,0) 100%),
      radial-gradient(ellipse 420px 200px at 320px 620px, rgba(44,58,34,0.9) 0%, rgba(44,58,34,0) 100%),
      radial-gradient(ellipse 520px 260px at 1000px 380px, rgba(16,22,15,0.85) 0%, rgba(16,22,15,0) 100%),
      linear-gradient(180deg,
        var(--sky-top) 0%,
        var(--sky-mist) 18%,
        var(--sky-haze) 24%,
        #4a5a4a 40%,
        var(--forest-moss) 55%,
        #2b4d52 68%,
        var(--forest-moss) 82%,
        var(--forest-deep) 100%);
  }
  .cover-title {
    position: absolute;
    right: 95px;
    top: 78px;
    text-align: right;
    color: var(--ink-white);
    font-family: "Montserrat", sans-serif;
    text-transform: uppercase;
  }
  .artist-name {
    margin: 0;
    font-weight: 600;
    font-size: 44px;
    line-height: 1;
    letter-spacing: 0.14em;
    margin-right: -0.14em;
  }
  .album-name {
    margin: 20px 0 0;
    font-weight: 200;
    font-size: 92px;
    line-height: 1;
    letter-spacing: 0.1em;
    margin-right: -0.1em;
  }
</style>
</head>
<body>
  <main class="album-cover">
    <div class="cover-artwork" role="img" aria-label="Misty forest landscape at sunrise with a winding teal river flowing between dark pine silhouettes"></div>
    <header class="cover-title">
      <p class="artist-name">Ilka Sorren</p>
      <h1 class="album-name">Cantarela</h1>
    </header>
  </main>
</body>
</html>
```